SKYVANTEX (drone photo and video) and Photogrammetry Services (mapping and 3D modeling)

We need a business card design for a SKYVANTEX. Our businesses provides (drone) Aerial Photo and Video Captures. However we also provide Photogrammetry (which is 3D modeling and mapping). We greatly value unique points of view taken of landscapes and subjects with aerial photography and videography. 3D modeling and mapping is the other area of focus and have an incredibly broad scope of applications and imaginative creativity.

Target Market(s)

Based out of Northern Virginia and serving the greater Virginia and Maryland areas

Industry/Entity Type

Drone Photo and video and Photogrammetry Services (mapping and 3D modeling)

Contact Information for Business Card

3D Models, Maps and Photo/Video Production name: Marcus Pettibone email: mqp@skyvantex.us website: skyvantex.us phone: 571-806-3394; please also include "Aerial Photo/Video and 3D Mapping/Modeling"

Requirements
Must have
• Please make this design vertical and double sided. The selection box is not letting me choose Double Sided but that is my wish. Incorporate uploaded LOGO and color scheme
Nice to have
• Preferably does not feel too crowded and balances not having an exaggerated amount of distracting detail
Should not have
• do not cram bullet points or text in long form

```html
<!DOCTYPE html>
<html lang="en">
<head>
<meta charset="utf-8">
<title>SKYVANTEX Business Card</title>
<link rel="stylesheet" href="https://fonts.googleapis.com/css2?family=Montserrat:wght@400;600;800&family=Oswald:wght@600&display=swap">
<style>
  :root {
    --bg: #3a3a3a;
    --ink: #0b0b0b;
    --paper: #ffffff;
    --orange: #f47a20;
    --red: #f5222d;
    --yellow: #fbb52b;
    --light: #f2f2f2;
  }
  * { box-sizing: border-box; margin: 0; padding: 0; }
  html, body { width: 1200px; height: 1200px; overflow: hidden; }
  body {
    background: var(--bg);
    font-family: "Montserrat", sans-serif;
    position: relative;
  }
  .card {
    position: absolute;
    top: 215px;
    width: 440px;
    height: 770px;
    overflow: hidden;
    box-shadow: 0 10px 30px rgba(0,0,0,.45);
  }
  .card--front { left: 120px; background: var(--ink); }
  .card--back { left: 640px; background: var(--paper); }

  .wordmark {
    position: absolute;
    left: 0; right: 0;
    display: flex;
    align-items: center;
    justify-content: center;
    gap: 14px;
  }
  .wordmark__dot {
    width: 38px; height: 38px; border-radius: 50%;
    background: var(--orange);
  }
  .wordmark__name {
    font-weight: 800;
    font-size: 46px;
    letter-spacing: 1px;
  }
  .card--front .wordmark { top: 330px; }
  .card--front .wordmark__name { color: var(--paper); }
  .card--back .wordmark { top: 190px; }
  .card--back .wordmark__name { color: var(--ink); }

  .tagline-band {
    position: absolute;
    left: 0; right: 0; bottom: 58px;
    height: 52px;
    background: linear-gradient(90deg, var(--red), var(--orange) 55%, var(--yellow));
    display: flex; align-items: center; justify-content: center;
  }
  .tagline-band__text {
    font-family: "Oswald", sans-serif;
    font-weight: 600;
    font-size: 21px;
    color: var(--paper);
    text-transform: uppercase;
    letter-spacing: .3px;
  }

  .back-divider { position: absolute; inset: 0; }

  .contact {
    position: absolute;
    left: 150px; top: 530px;
    color: var(--light);
  }
  .contact__name {
    color: var(--orange);
    font-weight: 600;
    font-size: 27px;
    letter-spacing: .5px;
    text-transform: uppercase;
    margin-bottom: 14px;
    margin-left: -40px;
  }
  .contact__list { list-style: none; }
  .contact__item {
    display: flex; align-items: center; gap: 14px;
    font-size: 21px; line-height: 44px;
  }
  .contact__icon { width: 24px; height: 24px; flex: none; }
</style>
</head>
<body>

<section class="card card--front" aria-label="Card front">
  <div class="wordmark">
    <span class="wordmark__dot"></span>
    <span class="wordmark__name">SKYVANTEX</span>
  </div>
  <div class="tagline-band">
    <span class="tagline-band__text">Aerial Photo/Video and 3D Mapping/Modeling</span>
  </div>
</section>

<section class="card card--back" aria-label="Card back">
  <div class="wordmark">
    <span class="wordmark__dot"></span>
    <span class="wordmark__name">SKYVANTEX</span>
  </div>

  <svg class="back-divider" viewBox="0 0 440 770" aria-hidden="true">
    <polygon points="0,620 200,440 440,410 440,770 0,770" fill="#0b0b0b"/>
    <polyline points="0,595 190,420 440,388" fill="none" stroke="#f47a20" stroke-width="9"/>
  </svg>

  <div class="contact">
    <p class="contact__name">Marcus Pettibone</p>
    <ul class="contact__list">
      <li class="contact__item">
        <svg class="contact__icon" viewBox="0 0 24 24"><path fill="#f47a20" d="M6.6 10.8a15 15 0 0 0 6.6 6.6l2.2-2.2a1 1 0 0 1 1-.25 11.4 11.4 0 0 0 3.6.57 1 1 0 0 1 1 1V20a1 1 0 0 1-1 1A17 17 0 0 1 3 4a1 1 0 0 1 1-1h3.5a1 1 0 0 1 1 1c0 1.25.2 2.45.57 3.57a1 1 0 0 1-.25 1z"/></svg>
        <span>571-806-3394</span>
      </li>
      <li class="contact__item">
        <svg class="contact__icon" viewBox="0 0 24 24" fill="none" stroke="#f47a20" stroke-width="2"><circle cx="12" cy="12" r="10"/><ellipse cx="12" cy="12" rx="4.5" ry="10"/><path d="M2 12h20M4 7h16M4 17h16"/></svg>
        <span>skyvantex.us</span>
      </li>
      <li class="contact__item">
        <svg class="contact__icon" viewBox="0 0 24 24"><rect x="2" y="5" width="20" height="14" fill="#f47a20"/><path d="M2 5l10 8 10-8" fill="none" stroke="#0b0b0b" stroke-width="1.6"/></svg>
        <span>mqp@skyvantex.us</span>
      </li>
    </ul>
  </div>
</section>

</body>
</html>
```